Pelham Design & Millwork needs a web presence. Looking for a unique Design so please submit an idea.

In brief, you should know the following about me: My company was established in 2001 and had been responsible for providing reasonable CAD Design and Custom Millwork ever since. My specialty is in the area Architectural CAD Design, Fabrication of Custom Millwork and Mouldings on a partime basis. Drawings and estimates done at a very reasonable cost. I look forward to working on your next project. Thanks in Advance, Boyd 
I would like one page to show thumbnails linked to some of past millwork projects and another page with thumbnails linking to some of my house designs. I assume last page will have contact information accessed from a link on home page. I already had a logo designed which I can supply you with to design home page around. As I indicated I have a regular full time job and do this for additional income and will move to full time when I have enough business.

I have attached the logo I had designed in a couple different colors. I have also uploaded some PDF's of files that I also considered before choosing the RED LOGO to give an ideas of how we could tweak the logo to better fit the website if need be. Text is wrong in those.

Thanks,
Boyd

I added my logo as a PDF side there seems to be a problem with scaling loge with the other file. Hope this helps.

Boyd

Evening,
I will be hosting this site on wavecrib. Its looks like it will get launched with wordpress?  What will be involved from getting your design up so I can upload project pictures and and text to areas you have set aside? I am also going to upload a couple jpg of a couple recent projects so you can put in so I can get a feel of what they will look like. Thanks for all your work to date! Boyd

I am not seeing alot of design variations or even many designers in fact. Is there something more from me you need? Do you need me to extend deadline?

Reason: It appears that your need some more time to submit some design changes. I will choose a design next week after changes have been submitted. Thanks for your time. Boyd

Reason: Designers needs a couple days to submit some last minute changes. Thanks for all your submissions! Boyd

Reason: Some last minute designs that I need to look at and give feedback on. I want to thank everyone for their designs and patience. Thanks again, Boyd

Evening All,

Upon discussion with a couple of the designers I want the design done in Word Press and I have increased budget the amount they said they would need to do it for. Thanks for all submissions so far but I am still looking for the special one that stands out among the rest! Boyd

I will not be extending deadline and choosing designer tomorrow morning so if you have anything else to add please do so tonight. Thanks for all your submissions. Boyd

Target Market(s)

Millwork projects will be generally local where as CAD Design Projects could be emailed anywhere. Probably more USA but who knows.

Industry/Entity Type

House

Font styles to use
Other font styles liked:
• Eras Medium ITC, Calibri or Designers choice.

Requirements
Must have
• Must tie in my logo on Homepage at least. Could even be somewhat transparent in background? I will let the designer work that out.
Nice to have
• Page to point to current and past Design projects on one page and millwork on another.
Should not have
• Target a large Corporate or Global environment since it is a small business right now.

```html
<!DOCTYPE html>
<html lang="en">
<head>
<meta charset="utf-8">
<title>Pelham Design &amp; Millwork</title>
<link rel="stylesheet" href="https://fonts.googleapis.com/css2?family=Arimo:wght@400;700&display=swap">
<style>
  :root {
    --nav-top: #fbc25a;
    --nav-bottom: #f7941d;
    --nav-link: #2f5d8c;
    --sky-deep: #2f9ad9;
    --sky-light: #8fd6f3;
    --panel: rgba(233, 243, 250, 0.9);
    --accent-orange: #f7941d;
    --body-text: #2b2b2b;
    --quote-red: #e3202a;
    --white: #ffffff;
    --ground: #2a4b26;
    --circle-light: #fdc94f;
    --circle-mid: #f9ad2c;
    --circle-deep: #f68a1f;
    --circle-darkest: #f47b20;
    --icon-blue: #2e5f8a;
    --logo-blue: #1f3f6a;
  }
  * { box-sizing: border-box; margin: 0; padding: 0; }
  html, body { width: 1200px; height: 795px; overflow: hidden; }
  body { font-family: "Arimo", Arial, sans-serif; background: var(--sky-deep); }

  .page {
    position: relative; width: 1200px; height: 795px; overflow: hidden;
    background: linear-gradient(180deg, var(--sky-deep) 0%, #4db3e6 45%, var(--sky-light) 100%);
  }

  .site-nav {
    position: absolute; left: 0; top: 0; width: 1200px; height: 53px;
    background: linear-gradient(180deg, var(--nav-top), var(--nav-bottom));
    z-index: 5;
  }
  .site-nav a {
    position: absolute; top: 14px; font-size: 20px; color: var(--nav-link); text-decoration: none;
  }
  .search-box {
    position: absolute; left: 952px; top: 12px; width: 180px; height: 32px;
    background: var(--white); border: 2px solid #8fcfc7; border-radius: 8px;
  }
  .search-box svg { position: absolute; right: 8px; top: 4px; }

  .house-scene {
    position: absolute; left: 700px; top: 220px; width: 500px; height: 575px;
    background: linear-gradient(160deg, rgba(255,255,255,0.55) 0%, #c9ccb0 40%, #9aa58e 75%, #6f7d6a 100%);
    clip-path: polygon(0 52%, 38% 30%, 48% 32%, 80% 0, 100% 4%, 100% 100%, 0 100%);
  }

  .brand-name {
    position: absolute; left: 470px; top: 110px; width: 270px; text-align: center;
    color: var(--logo-blue); font-size: 34px; font-weight: 400; line-height: 1.15;
  }
  .brand-name .mark {
    display: block; width: 56px; height: 56px; margin: 0 auto 14px;
    border-radius: 50%; background: var(--logo-blue);
  }

  .slide-arrow {
    position: absolute; width: 64px; height: 64px; border-radius: 50%;
    background: rgba(255,255,255,0.15);
  }
  .slide-arrow.prev { left: 7px; top: 320px; }
  .slide-arrow.next { left: 1126px; top: 314px; background: rgba(255,255,255,0.1); }

  .ground-band {
    position: absolute; left: 0; top: 709px; width: 715px; height: 86px; background: var(--ground);
  }

  .welcome-panel {
    position: absolute; left: 94px; top: 341px; width: 467px; height: 271px;
    background: var(--panel); border-radius: 14px; padding: 30px 38px;
  }
  .welcome-panel h1 {
    color: var(--accent-orange); font-size: 33px; font-weight: 400; line-height: 1.27; margin-bottom: 12px;
  }
  .welcome-panel p { color: var(--body-text); font-size: 16px; line-height: 1.27; }

  .quote-button {
    position: absolute; left: 711px; top: 419px; width: 354px; height: 80px;
    background: var(--quote-red); border-radius: 14px; color: var(--white);
    font-size: 25px; text-align: center; line-height: 80px; text-decoration: none;
  }

  .quick-links { position: absolute; left: 0; top: 0; }
  .quick-link {
    position: absolute; top: 590px; width: 140px; text-align: center; color: var(--white);
    text-decoration: none; font-size: 18px; line-height: 1.2;
  }
  .quick-link .circle {
    display: flex; align-items: center; justify-content: center;
    width: 112px; height: 112px; border-radius: 50%; margin: 0 auto 12px;
  }
  .circle-about { background: var(--circle-light); color: var(--icon-blue); font-size: 30px; font-weight: 700; }
  .circle-projects { background: var(--circle-mid); }
  .circle-houses { background: var(--circle-deep); }
  .circle-contact { background: var(--circle-darkest); color: var(--icon-blue); font-size: 70px; font-weight: 700; }
</style>
</head>
<body>
<div class="page">
  <nav class="site-nav">
    <a href="#" style="left:91px">About</a>
    <a href="#" style="left:182px">Past millwork projects</a>
    <a href="#" style="left:427px">House designs</a>
    <a href="#" style="left:601px">Request free quote</a>
    <a href="#" style="left:816px">Contact</a>
    <div class="search-box">
      <svg width="24" height="24" viewBox="0 0 24 24" aria-hidden="true">
        <circle cx="9" cy="9" r="6.5" fill="none" stroke="#222" stroke-width="2.6"/>
        <line x1="14" y1="14" x2="22" y2="22" stroke="#222" stroke-width="3.4" stroke-linecap="round"/>
      </svg>
    </div>
  </nav>

  <div class="house-scene" role="img" aria-label="Two-storey house with arched windows overlaid on architectural floor plan drawings"></div>

  <div class="brand-name"><span class="mark"></span>Boyd Pelham<br>Design &amp; Millwork</div>

  <div class="slide-arrow prev"><svg width="64" height="64" viewBox="0 0 64 64" aria-hidden="true"><polyline points="38,18 24,32 38,46" fill="none" stroke="rgba(255,255,255,0.35)" stroke-width="3"/></svg></div>
  <div class="slide-arrow next"><svg width="64" height="64" viewBox="0 0 64 64" aria-hidden="true"><polyline points="26,18 40,32 26,46" fill="none" stroke="rgba(255,255,255,0.3)" stroke-width="3"/></svg></div>

  <div class="ground-band"></div>

  <section class="welcome-panel">
    <h1>Welcome to Boyd Pelham Design &amp; Millwork</h1>
    <p>Do you need help with Millwork or CAD Design for your project? Then you have come to the right place. Get specialized help in the area Architectural CAD Design, Fabrication of Custom Millwork and Mouldings. Request a free quote today!</p>
  </section>

  <a class="quote-button" href="#">REQUEST FREE QUOTE</a>

  <div class="quick-links">
    <a class="quick-link" href="#" style="left:71px"><span class="circle circle-about">About</span>About</a>
    <a class="quick-link" href="#" style="left:202px"><span class="circle circle-projects" role="img" aria-label="Hand saw icon"></span>Past Millwork<br>Projects</a>
    <a class="quick-link" href="#" style="left:333px"><span class="circle circle-houses">
      <svg width="74" height="60" viewBox="0 0 74 60" aria-hidden="true">
        <polygon points="37,2 72,24 2,24" fill="#2e5f8a"/>
        <rect x="8" y="24" width="58" height="34" fill="#2e5f8a"/>
        <rect x="14" y="30" width="9" height="9" fill="#f68a1f"/>
        <rect x="51" y="30" width="9" height="9" fill="#f68a1f"/>
        <rect x="14" y="44" width="9" height="9" fill="#f68a1f"/>
        <rect x="51" y="44" width="9" height="9" fill="#f68a1f"/>
        <rect x="31" y="38" width="12" height="20" fill="#f68a1f"/>
      </svg></span>House<br>Designs</a>
    <a class="quick-link" href="#" style="left:467px"><span class="circle circle-contact">@</span>Contact</a>
  </div>
</div>
</body>
</html>
```